Brochure for Coral Drift Voyages

A new brochure/A4 Flyer for our Coral Drift Voyages.
We have been operating a successful small business for 3 years in The Whisundays, QLD, Australia. The heart of the Great Barrier Reef.
We offer one-hour Coral Drift Voyages 3 times a day on our zero emissions electric boat for up to 8 guests.

Target Market(s)

All tourists visiting the Whitsundays. All ages and abilities

Industry/Entity Type

Tourism

Other font styles liked:
• Easy to read

Colors
0054AA
0677BA
7BADD7
CADEEF
E8F1F8
00AB8E
00BBA5
67D7C9
C6EFE9
E9F9F6

Requirements
Must have
• High impact font page. It's all about Bluewake Trips for one-hour.
Nice to have
• Bluewake Trips in top quarter/third of front page with a picture of a turtle
Should not have
• Not too much distraction on front page. More info on the back

```html
<!DOCTYPE html>
<html lang="en">
<head>
<meta charset="utf-8">
<title>Hushwater Cruises – Bluewake Trips Flyer</title>
<link href="https://fonts.googleapis.com/css2?family=Poppins:wght@400;500;600;700;800;900&family=Oswald:wght@500&family=Allura&display=swap" rel="stylesheet">
<style>
  :root{
    --backdrop:#d9d9d9;
    --night:#020d18;
    --ink:#1b1b22;
    --logo-navy:#1d2a4a;
    --teal:#3a86a8;
    --price-blue:#a9c9ee;
    --pill:#a9a6c9;
    --white:#ffffff;
    --band:#123a4b;
    --text-grey:#2a2a2a;
  }
  *{box-sizing:border-box;margin:0;padding:0}
  html,body{width:1200px;height:1200px;overflow:hidden;background:var(--backdrop)}
  body{position:relative;font-family:'Poppins',sans-serif}

  .page{position:absolute;top:224px;width:526px;height:744px;overflow:hidden;box-shadow:0 2px 6px rgba(0,0,0,.18)}
  .page--front{left:52px;background:var(--night)}
  .page--back{left:617px;background:var(--white)}

  /* front */
  .front-photo{position:absolute;left:0;top:0;width:526px;height:560px;
    background:linear-gradient(180deg,#5d95cc 0%,#8fbce0 22%,#6f7f5e 32%,#4f8db6 45%,#2f79a8 60%,#274560 78%,var(--night) 100%)}
  .brand{position:absolute;top:62px;left:0;width:100%;display:flex;justify-content:center;align-items:center;gap:8px}
  .brand__dot{width:10px;height:10px;border-radius:50%;background:var(--logo-navy)}
  .brand__name{font-size:26px;font-weight:500;color:var(--logo-navy);letter-spacing:1px}
  .hero-title{position:absolute;left:58px;top:514px;font-weight:900;font-size:72px;line-height:1;color:var(--white);letter-spacing:-1.5px}
  .hero-script{position:absolute;left:92px;top:562px;font-family:'Allura',cursive;font-size:88px;line-height:1;color:var(--teal)}
  .meeting{position:absolute;left:257px;top:608px;list-style:none;color:var(--white);font-size:9.4px;line-height:1.2}
  .meeting li{display:flex;gap:4px;margin-bottom:6px}
  .meeting svg{flex:none;margin-top:1px}
  .front-web{position:absolute;left:0;width:100%;top:694px;display:flex;justify-content:center;align-items:center;gap:10px;color:var(--white);font-size:13.5px;letter-spacing:1.6px}

  /* back top */
  .reef-photo{position:absolute;left:0;top:0;width:526px;height:338px;
    background:radial-gradient(ellipse at 70% 0%,#2b7aa5 0%,transparent 55%),
      radial-gradient(ellipse at 78% 58%,#8a5a3a 0%,#4a4a4a 12%,transparent 26%),
      linear-gradient(180deg,#1b5f86 0%,#0f4566 45%,#0a2f48 100%)}
  .tours-head{position:absolute;left:30px;top:34px;font-weight:800;font-size:50px;color:var(--white);line-height:1}
  .tours-sub{position:absolute;left:202px;top:38px;font-weight:700;font-size:18px;color:var(--white)}
  .tours-script{position:absolute;left:212px;top:46px;font-family:'Allura',cursive;font-size:42px;color:var(--white)}
  .rule{position:absolute;left:34px;width:254px;height:1px;background:rgba(255,255,255,.35)}
  .tour-name{position:absolute;left:34px;color:var(--white);font-weight:700;font-size:12.4px;line-height:1.3;white-space:nowrap}
  .pill{position:absolute;background:var(--pill);color:var(--white);font-weight:600;font-size:8.6px;padding:2px 9px;border-radius:10px;white-space:nowrap}
  .price{position:absolute;font-family:'Oswald',sans-serif;font-weight:500;font-size:36px;line-height:1;color:var(--price-blue)}
  .price sup{font-size:15px;vertical-align:top;position:relative;top:2px}
  .price-note{position:absolute;color:var(--white);font-size:9.5px;line-height:1.25}
  .divider{position:absolute;top:250px;height:44px;border-left:1px dashed rgba(255,255,255,.8)}

  /* back bottom */
  .charter-photo{position:absolute;left:43px;top:365px;width:210px;height:220px;background:var(--white);padding:4px;box-shadow:0 1px 4px rgba(0,0,0,.25)}
  .charter-photo div{width:100%;height:100%;background:linear-gradient(180deg,#f07a2a 0%,#e35a1a 30%,#3a2418 50%,#c8521c 62%,#2a1a14 100%)}
  .snap{position:absolute;width:100px;height:98px;background:var(--white);padding:4px;box-shadow:0 2px 6px rgba(0,0,0,.3)}
  .snap div{width:100%;height:100%}
  .snap--one{left:42px;top:544px;transform:rotate(-18deg)}
  .snap--one div{background:linear-gradient(180deg,#cfe6f0,#8a6a50)}
  .snap--two{left:140px;top:566px;transform:rotate(15deg)}
  .snap--two div{background:linear-gradient(180deg,#7fd0e6,#c9a58a)}
  .charter-title{position:absolute;left:278px;top:360px;font-weight:700;font-size:17px;line-height:1.18;color:var(--ink)}
  .charter-title span{color:var(--teal)}
  .charter-copy{position:absolute;left:278px;width:206px;font-size:8.6px;line-height:10.6px;text-align:justify;color:var(--text-grey)}
  .charter-copy--intro{top:405px}
  .charter-copy--vessel{top:496px}
  .challenge{position:absolute;left:278px;top:627px;font-size:14px;line-height:1.2;color:var(--ink)}
  .challenge strong{color:var(--teal);font-weight:700;font-size:13.5px}
  .contacts{position:absolute;left:42px;top:692px;display:flex;gap:10px;font-size:10px;color:var(--ink);align-items:center}
  .contacts span{display:flex;align-items:center;gap:4px}
  .foot-band{position:absolute;left:0;bottom:0;width:100%;height:10px;background:var(--band)}
</style>
</head>
<body>

<section class="page page--front">
  <div class="front-photo" role="img" aria-label="Photo: guest waving from an electric boat on calm water with a turtle surfacing, hills and village behind"></div>
  <div class="brand"><span class="brand__dot"></span><span class="brand__name">Hushwater Cruises</span></div>
  <h1 class="hero-title">BLUEWAKE</h1>
  <div class="hero-script">Trips</div>
  <ul class="meeting">
    <li><svg width="8" height="8" viewBox="0 0 8 8"><circle cx="4" cy="4" r="4" fill="#3a86a8"/><path d="M2 4l1.4 1.4L6 2.8" stroke="#fff" fill="none" stroke-width="1"/></svg><span>Meet outside Marlow Bar<br>&amp; Restaurant</span></li>
    <li><svg width="8" height="8" viewBox="0 0 8 8"><circle cx="4" cy="4" r="4" fill="#3a86a8"/><path d="M2 4l1.4 1.4L6 2.8" stroke="#fff" fill="none" stroke-width="1"/></svg><span>Reefside Marina (North Complex)<br>10 minutes prior to departure</span></li>
    <li><svg width="8" height="8" viewBox="0 0 8 8"><circle cx="4" cy="4" r="4" fill="#3a86a8"/><path d="M2 4l1.4 1.4L6 2.8" stroke="#fff" fill="none" stroke-width="1"/></svg><span>Maximum 8 guests</span></li>
  </ul>
  <div class="front-web">
    <svg width="14" height="14" viewBox="0 0 14 14"><path d="M1 1l12 5-5 1.5L6.5 13z" fill="#3a86a8"/></svg>
    <span>www.hushwatercruises.com.au</span>
  </div>
</section>

<section class="page page--back">
  <div class="reef-photo" role="img" aria-label="Photo: sea turtle swimming over an underwater reef with light rays"></div>
  <div class="tours-head">TOURS</div>
  <div class="tours-sub">AVAILABLE</div>
  <div class="tours-script">Daily</div>
  <div class="rule" style="top:98px"></div>

  <div class="tour-name" style="top:114px">MIMOSA MORNING CRUISE</div>
  <div class="pill" style="left:217px;top:114px">9.30AM</div>
  <div class="price" style="left:34px;top:133px"><sup>$</sup>85PP</div>
  <div class="price-note" style="left:119px;top:135px">Includes Mimosas<br>Orange Juice<br>Bubbles</div>

  <div class="rule" style="top:182px"></div>
  <div class="tour-name" style="top:193px">ONE-HOUR CORAL<br>DRIFT VOYAGES<br>OPERATE DAILY AT</div>
  <div class="pill" style="left:170px;top:196px">11.00AM &amp; 12.30PM</div>

  <div class="price" style="left:34px;top:246px"><sup>$</sup>69PP</div>
  <div class="price-note" style="left:45px;top:284px">Adults (16+)</div>
  <div class="divider" style="left:124px"></div>
  <div class="price" style="left:137px;top:246px"><sup>$</sup>55PP</div>
  <div class="price-note" style="left:141px;top:284px">Child (1-15yo)</div>
  <div class="divider" style="left:227px"></div>
  <div class="price-note" style="left:244px;top:260px"><strong>Infants</strong><br>FOC (0-1)</div>

  <div class="charter-photo"><div role="img" aria-label="Photo: sunset over the water with a glass of bubbles on the boat deck"></div></div>
  <div class="snap snap--one"><div role="img" aria-label="Photo: skipper and guest at the helm"></div></div>
  <div class="snap snap--two"><div role="img" aria-label="Photo: guests toasting on board"></div></div>

  <h2 class="charter-title">PRIVATE CHARTERS<br><span>AVAILABLE</span></h2>
  <p class="charter-copy charter-copy--intro">Embark on an extraordinary and environmentally responsible journey by stepping aboard Airlie Beach’s most unique tour. Join us for an intimate and serene adventure where sustainability meets luxury, creating memories that are as gentle on the environment as they are unforgettable.</p>
  <p class="charter-copy charter-copy--vessel">With a maximum capacity of just 8 passengers, our charming vessel <strong>‘Marigold”</strong> stands out as the only electric boat in the Whitsundays. Experience the magic of spotting turtles in eco-friendly luxury, gliding though calm waters with our whisper-quiet, fume-free electric boat. Be on the lookout for the endangered loggerhead and green sea turtles. Immerse yourself in a serene journey as we tour through Turtle Bay, around Pigeon Island and the local foreshore, then back past the million-dollar yachts in the Reefside Marina.</p>
  <p class="challenge">Can you beat our<br><strong>‘turtle count’ record?</strong></p>

  <div class="contacts">
    <span><svg width="11" height="11" viewBox="0 0 12 12"><path d="M2.5 1l2 2.5-1 1.2a7 7 0 0 0 3.8 3.8l1.2-1 2.5 2-1.2 1.5C5.5 11 1 6.5 1 2.2z" fill="#3a86a8"/></svg>+61 400 000 123</span>
    <span><svg width="12" height="9" viewBox="0 0 12 9"><rect width="12" height="9" fill="#3a86a8"/><path d="M0 0l6 5 6-5" stroke="#fff" fill="none"/></svg>info@hushwatercruises.com.au</span>
    <span><svg width="11" height="11" viewBox="0 0 12 12"><circle cx="6" cy="6" r="5.2" stroke="#3a86a8" fill="none"/><ellipse cx="6" cy="6" rx="2.3" ry="5.2" stroke="#3a86a8" fill="none"/><path d="M1 6h10" stroke="#3a86a8"/></svg>www.hushwatercruises.com.au</span>
  </div>
  <div class="foot-band"></div>
</section>

</body>
</html>
```